Mailer Postcard for Potential Bankruptcy Clients

The postcard will be printed at 8.5"x6" to abide by the specification at the following link: https://www.mailvortex.example/art-upload/guide/. I want an attractive two sided post card that includes my logo (see attachment). The design would have to have room for the website address, phone number, two location addresses and give them information about a civil action pending against them (You are being sued in X county (case# xxyx). We can help.). I don't really like the visuals of the attached postcard, so please use as a general guide for what I am trying to do. Ultimately, I want an ad that gets people to call me so I can help them.

I also want it to be compatible with the website (CreditHarbor.Legal).

Target Market(s)

Potential bankruptcy clients.

Industry/Entity Type

Legal

Colors

Designer to choose colors to be used in the design.

Requirements
Must have
• Phone number, addresses, website, and place for text regarding pending legal action against the receiver. Should say something to the effect: You have a pending legal action in (county name) County (court name [superior, magistrate, ect.]). Let us help you deal with it responsibly.
• Please note the design specifications at this link:

```html
<!DOCTYPE html>
<html lang="en">
<head>
<meta charset="utf-8">
<title>Credit Harbor Law Group – Mailer Postcard</title>
<link rel="stylesheet" href="https://fonts.googleapis.com/css2?family=Oswald:wght@300;500;600&family=Mulish:wght@400;600;700&display=swap">
<style>
  :root {
    --green: #84c18f;
    --green-deep: #5fa96f;
    --green-pale: #e7f3e6;
    --ink: #2c3430;
    --ink-soft: #4a524d;
    --paper: #ffffff;
    --stage: #e9eaea;
    --line: #c9cccb;
  }
  html, body { margin: 0; padding: 0; }
  body {
    width: 1051px; height: 1200px; overflow: hidden;
    background: var(--stage);
    font-family: "Mulish", sans-serif;
  }
  .postcard {
    position: absolute; left: 85px; width: 880px; height: 527px;
    background: var(--paper);
    box-shadow: 0 4px 18px rgba(0,0,0,.18);
    overflow: hidden;
  }
  .postcard--front { top: 40px; }
  .postcard--back { top: 633px; }
  .postcard svg { display: block; width: 880px; height: 527px; }
  .headline-light { font-family: "Oswald", sans-serif; font-weight: 300; fill: var(--ink); }
  .headline-bold { font-family: "Oswald", sans-serif; font-weight: 600; fill: var(--ink); }
  .section-title { font-family: "Mulish", sans-serif; font-weight: 700; fill: var(--green-deep); }
  .section-heading { font-family: "Oswald", sans-serif; font-weight: 500; fill: var(--ink); }
  .small-copy { font-family: "Mulish", sans-serif; font-weight: 400; fill: var(--ink-soft); }
  .service-label { font-family: "Mulish", sans-serif; font-weight: 600; fill: var(--ink); font-size: 13px; text-anchor: middle; }
  .badge-text { font-family: "Oswald", sans-serif; font-weight: 300; fill: var(--paper); text-anchor: middle; }
  .brand-name { font-family: "Mulish", sans-serif; font-weight: 700; fill: var(--ink); }
  .brand-sub { font-family: "Mulish", sans-serif; font-weight: 400; fill: var(--ink-soft); }
  .list-item { font-family: "Mulish", sans-serif; font-weight: 400; fill: var(--ink); font-size: 11.5px; }
  .contact-item { font-family: "Mulish", sans-serif; font-weight: 600; fill: var(--ink); font-size: 11.5px; }
  .notice-title { font-family: "Mulish", sans-serif; font-weight: 700; fill: var(--ink); font-size: 12px; }
  .notice-copy { font-family: "Mulish", sans-serif; font-weight: 400; fill: var(--ink); font-size: 11px; }
  .box-label { font-family: "Mulish", sans-serif; font-weight: 400; fill: var(--ink); font-size: 13px; text-anchor: middle; }
</style>
</head>
<body>

<!-- Front side -->
<section class="postcard postcard--front" aria-label="Postcard front side">
  <svg viewBox="0 0 880 527" xmlns="http://www.w3.org/2000/svg">
    <defs>
      <linearGradient id="header-wash" x1="0" y1="0" x2="1" y2="1">
        <stop offset="0" stop-color="#bfe0c1"/>
        <stop offset="1" stop-color="#f4f9f3"/>
      </linearGradient>
      <linearGradient id="services-wash" x1="0" y1="0" x2="1" y2="0">
        <stop offset="0" stop-color="#8cc595"/>
        <stop offset="1" stop-color="#b8dcb9"/>
      </linearGradient>
      <radialGradient id="photo-glow" cx="0.62" cy="0.5" r="0.6">
        <stop offset="0" stop-color="#a88559"/>
        <stop offset="0.45" stop-color="#5b4228"/>
        <stop offset="1" stop-color="#17120e"/>
      </radialGradient>
      <linearGradient id="wood-tone" x1="0" y1="0" x2="1" y2="1">
        <stop offset="0" stop-color="#8a4a30"/>
        <stop offset="1" stop-color="#5c2d1d"/>
      </linearGradient>
      <clipPath id="panel-clip">
        <path d="M0 0 H345 C470 10 590 60 622 120 L612 330 C600 420 560 490 505 527 H0 Z"/>
      </clipPath>
    </defs>

    <!-- photo area: globe and scales of justice -->
    <rect class="photo-globe" x="300" y="0" width="580" height="425" fill="url(#photo-glow)"
          role="img" aria-label="Photo of a bronze globe with scales of justice on a dark background"/>

    <!-- brand panel, lower right -->
    <rect class="brand-panel" x="450" y="420" width="430" height="107" fill="var(--paper)"/>

    <!-- left content panel -->
    <g clip-path="url(#panel-clip)">
      <rect x="0" y="0" width="640" height="527" fill="url(#services-wash)"/>
      <rect x="0" y="0" width="640" height="178" fill="url(#header-wash)"/>
      <rect x="0" y="186" width="640" height="48" fill="var(--paper)"/>
      <rect class="photo-table" x="0" y="418" width="640" height="109" fill="url(#wood-tone)"
            role="img" aria-label="Photo of letter tiles spelling LAW on a wooden table"/>
    </g>
    <path d="M345 0 C470 10 590 60 622 120 L612 330 C600 420 560 490 505 527" fill="none" stroke="var(--paper)" stroke-width="6"/>
    <path d="M349 0 C474 10 594 60 626 120 L616 330 C604 420 564 490 509 527" fill="none" stroke="var(--ink)" stroke-width="1.5"/>

    <!-- headline -->
    <text class="headline-light" x="14" y="82" font-size="66">GET OUT OF</text>
    <text class="headline-bold" x="14" y="158" font-size="46" textLength="585" lengthAdjust="spacingAndGlyphs">DEBT &amp; RESTORE YOUR CREDIT</text>

    <!-- services band -->
    <text class="section-title" x="14" y="220" font-size="28">OUR SERVICES</text>
    <text class="small-copy" x="228" y="206" font-size="10">Below are a few services that we offer. Contact us to</text>
    <text class="small-copy" x="228" y="219" font-size="10">get more details and see what we can do for you.</text>

    <!-- services grid -->
    <g class="services-grid">
      <line x1="195" y1="248" x2="195" y2="410" stroke="#ffffff" stroke-opacity=".35"/>
      <line x1="350" y1="248" x2="350" y2="410" stroke="#ffffff" stroke-opacity=".35"/>

      <g class="service">
        <circle cx="117" cy="264" r="12" fill="var(--green-deep)" stroke="#fff" stroke-width="1.5"/>
        <path d="M111 266 L117 260 L123 266 M113 265 V270 H121 V265" fill="none" stroke="#fff" stroke-width="1.5"/>
        <text class="service-label" x="117" y="296">Mortgage Loan</text>
        <text class="service-label" x="117" y="311">Modifications</text>
      </g>
      <g class="service">
        <circle cx="272" cy="264" r="12" fill="var(--green-deep)" stroke="#fff" stroke-width="1.5"/>
        <rect x="267" y="257" width="10" height="13" fill="none" stroke="#fff" stroke-width="1.5"/>
        <text class="service-label" x="272" y="296">Credit Report</text>
        <text class="service-label" x="272" y="311">Inaccuracies &amp; Errors</text>
      </g>
      <g class="service">
        <circle cx="429" cy="264" r="12" fill="var(--green-deep)" stroke="#fff" stroke-width="1.5"/>
        <path d="M420 263 L429 258 L438 263 L429 268 Z" fill="#fff"/>
        <text class="service-label" x="429" y="302">Student Loans</text>
      </g>
      <g class="service">
        <circle cx="117" cy="354" r="12" fill="var(--green-deep)" stroke="#fff" stroke-width="1.5"/>
        <path d="M110 352 H124 M117 347 V362 M112 352 L110 358 H114 Z M122 352 L120 358 H124 Z" fill="none" stroke="#fff" stroke-width="1.3"/>
        <text class="service-label" x="117" y="386">Debt Collection</text>
        <text class="service-label" x="117" y="401">Violations</text>
      </g>
      <g class="service">
        <circle cx="272" cy="354" r="12" fill="var(--green-deep)" stroke="#fff" stroke-width="1.5"/>
        <path d="M265 360 H279 M266 351 L272 347 L278 351 Z M267 352 V359 M272 352 V359 M277 352 V359" fill="none" stroke="#fff" stroke-width="1.3"/>
        <text class="service-label" x="272" y="390">Bankruptcy</text>
      </g>
      <g class="service">
        <circle cx="429" cy="354" r="12" fill="var(--green-deep)" stroke="#fff" stroke-width="1.5"/>
        <rect x="423" y="349" width="12" height="10" fill="none" stroke="#fff" stroke-width="1.5"/>
        <text class="service-label" x="429" y="386">Free Credit</text>
        <text class="service-label" x="429" y="401">Rebuilding Program</text>
      </g>
    </g>

    <!-- start now badge -->
    <g class="start-badge">
      <circle cx="566" cy="314" r="46" fill="var(--green)" stroke="#fff" stroke-width="4"/>
      <circle cx="566" cy="314" r="39" fill="none" stroke="#fff" stroke-opacity=".6" stroke-width="1"/>
      <text class="badge-text" x="566" y="308" font-size="25" transform="rotate(-10 566 314)">START</text>
      <text class="badge-text" x="566" y="337" font-size="29" transform="rotate(-10 566 314)">NOW</text>
    </g>

    <!-- brand lockup -->
    <g class="brand-lockup">
      <rect x="598" y="448" width="52" height="52" fill="var(--green)"/>
      <line x1="664" y1="440" x2="664" y2="512" stroke="var(--green)" stroke-width="2"/>
      <text class="brand-name" x="676" y="470" font-size="26">Credit Harbor</text>
      <text class="brand-name" x="676" y="491" font-size="13" letter-spacing="3">LAW GROUP</text>
      <text class="brand-sub" x="676" y="508" font-size="11">by Attorney M. Calloway</text>
    </g>
  </svg>
</section>

<!-- Back side -->
<section class="postcard postcard--back" aria-label="Postcard back side">
  <svg viewBox="0 0 880 527" xmlns="http://www.w3.org/2000/svg">
    <defs>
      <linearGradient id="back-wash" x1="0" y1="0" x2="1" y2="0">
        <stop offset="0" stop-color="#8cc595"/>
        <stop offset="1" stop-color="#c2e1c2"/>
      </linearGradient>
    </defs>

    <!-- left info panel -->
    <path class="info-panel" d="M0 14 H190 C310 18 440 62 468 150 L478 380 C470 450 440 500 404 527 H0 Z" fill="url(#back-wash)"/>
    <path d="M194 14 C314 18 444 62 472 150 L482 380 C474 450 444 500 408 527" fill="none" stroke="var(--ink)" stroke-width="1.5"/>

    <text class="section-heading" x="14" y="56" font-size="28">WHO ARE WE?</text>
    <line x1="14" y1="64" x2="160" y2="64" stroke="var(--ink)" stroke-width="1.5"/>

    <g class="offer-list">
      <g><circle cx="20" cy="108" r="5" fill="none" stroke="var(--ink)"/><path d="M17.5 108 L19.5 110 L22.5 106" fill="none" stroke="var(--ink)" stroke-width="1.2"/><text class="list-item" x="32" y="112">Free Credit Education Program</text></g>
      <g><circle cx="20" cy="139" r="5" fill="none" stroke="var(--ink)"/><path d="M17.5 139 L19.5 141 L22.5 137" fill="none" stroke="var(--ink)" stroke-width="1.2"/><text class="list-item" x="32" y="143">$0 Down Bankruptcy Options</text></g>
      <g><circle cx="20" cy="170" r="5" fill="none" stroke="var(--ink)"/><path d="M17.5 170 L19.5 172 L22.5 168" fill="none" stroke="var(--ink)" stroke-width="1.2"/><text class="list-item" x="32" y="174">Stop Collection Calls</text></g>
      <g><circle cx="20" cy="201" r="5" fill="none" stroke="var(--ink)"/><path d="M17.5 201 L19.5 203 L22.5 199" fill="none" stroke="var(--ink)" stroke-width="1.2"/><text class="list-item" x="32" y="205">Stop Foreclosures &amp; Repossessions</text></g>
      <g><circle cx="20" cy="232" r="5" fill="none" stroke="var(--ink)"/><path d="M17.5 232 L19.5 234 L22.5 230" fill="none" stroke="var(--ink)" stroke-width="1.2"/><text class="list-item" x="32" y="236">Stop Garnishments</text></g>

      <g><circle cx="246" cy="108" r="5" fill="none" stroke="var(--ink)"/><path d="M243.5 108 L245.5 110 L248.5 106" fill="none" stroke="var(--ink)" stroke-width="1.2"/><text class="list-item" x="258" y="112">Fix Credit Report Errors</text></g>
      <g><circle cx="246" cy="139" r="5" fill="none" stroke="var(--ink)"/><path d="M243.5 139 L245.5 141 L248.5 137" fill="none" stroke="var(--ink)" stroke-width="1.2"/><text class="list-item" x="258" y="143">Prosecute Illegal Debt Collection</text><text class="list-item" x="258" y="157">Practices</text></g>
      <g><circle cx="246" cy="184" r="5" fill="none" stroke="var(--ink)"/><path d="M243.5 184 L245.5 186 L248.5 182" fill="none" stroke="var(--ink)" stroke-width="1.2"/><text class="list-item" x="258" y="188">Prosecute Post Discharge Violations</text></g>
      <g><circle cx="246" cy="215" r="5" fill="none" stroke="var(--ink)"/><path d="M243.5 215 L245.5 217 L248.5 213" fill="none" stroke="var(--ink)" stroke-width="1.2"/><text class="list-item" x="258" y="219">Student Loan Representation</text></g>
    </g>

    <!-- about band -->
    <path d="M0 276 H474 L476 360 C420 368 300 372 0 366 Z" fill="var(--paper)"/>
    <g class="small-copy" font-size="9">
      <text x="14" y="294">We are a Georgia Law Firm that is dedicated to being a one-stop shop for all debt woes that</text>
      <text x="14" y="307">Georgians face. We are experienced bankruptcy attorneys that understand that people need more</text>
      <text x="14" y="320">than just a bankruptcy lawyer. People need someone that is experienced in handling all of the</text>
      <text x="14" y="333">practical aspects of avoiding bankruptcy, recovering from bankruptcy quickly, tackling stubborn</text>
      <text x="14" y="346">student loans, and punishing abusive debt collectors when they violate the law. If you came to</text>
      <text x="14" y="359">this website and have read this far, you should contact us to see if we can help you.</text>
    </g>

    <!-- contact -->
    <text class="section-heading" x="14" y="412" font-size="28">CONTACT US</text>
    <line x1="14" y1="420" x2="140" y2="420" stroke="var(--ink)" stroke-width="1.5"/>
    <g class="contact-list">
      <circle cx="20" cy="441" r="3.5" fill="var(--ink)"/><text class="contact-item" x="30" y="445">418 Linden Ave., NW Suite #1400 Atlanta, Georgia 30303</text>
      <circle cx="20" cy="465" r="3.5" fill="var(--ink)"/><text class="contact-item" x="30" y="469">2215 Maple Row Douglasville, Georgia 30134</text>
      <circle cx="20" cy="489" r="3.5" fill="var(--ink)"/><text class="contact-item" x="30" y="493">(404) 555-0172</text>
      <circle cx="20" cy="513" r="3.5" fill="var(--ink)"/><text class="contact-item" x="30" y="517">www.creditharbor.legal</text>
    </g>

    <!-- brand lockup -->
    <g class="brand-lockup">
      <rect x="500" y="26" width="36" height="36" fill="var(--green)"/>
      <line x1="546" y1="22" x2="546" y2="70" stroke="var(--green)" stroke-width="1.5"/>
      <text class="brand-name" x="554" y="44" font-size="18">Credit Harbor</text>
      <text class="brand-name" x="554" y="58" font-size="9" letter-spacing="2">LAW GROUP</text>
      <text class="brand-sub" x="554" y="70" font-size="7.5">by Attorney M. Calloway</text>
    </g>

    <!-- stamp box -->
    <rect x="738" y="12" width="128" height="120" fill="none" stroke="var(--line)" stroke-width="1.5"/>
    <text class="box-label" x="802" y="77">STAMP</text>

    <!-- pending legal action notice -->
    <g class="legal-notice">
      <rect x="500" y="146" width="366" height="62" fill="var(--green-pale)" stroke="var(--green)" stroke-width="1.5"/>
      <text class="notice-title" x="512" y="166">You have a pending legal action in ____________ County</text>
      <text class="notice-copy" x="512" y="182">(______________ Court, Case # ____________).</text>
      <text class="notice-copy" x="512" y="198">Let us help you deal with it responsibly.</text>
    </g>

    <!-- address lines -->
    <g class="address-lines" stroke="var(--line)" stroke-width="1.5">
      <line x1="540" y1="240" x2="866" y2="240"/>
      <line x1="540" y1="268" x2="866" y2="268"/>
      <line x1="540" y1="296" x2="866" y2="296"/>
      <line x1="540" y1="324" x2="866" y2="324"/>
      <line x1="540" y1="352" x2="866" y2="352"/>
    </g>

    <!-- barcode clear zone -->
    <rect class="barcode-zone" x="494" y="456" width="372" height="58" fill="none" stroke="var(--line)" stroke-width="1.5"/>
    <text class="box-label" x="680" y="490">BARCODE</text>
  </svg>
</section>

</body>
</html>
```